Acupuncture Medspa needs a business card design

I need a business card design that looks professional, has a spa-like quality and can offer a promo on the back. Initial promo is "First session free". The tagline of NeedleNook is: Refresh, Restore, Rejuvenate.

NeedleNook is a membership-based acupuncture medspa that offers acupuncture, cupping, and herbal therapies. Members choose between the "Refresh" membership which is for stress relief, or "Restore" which is for treating health conditions, and lastly "Rejuvenate" which is for natural facial enhancement.

Industry/Entity Type

Health And Wellness

Contact Information for Business Card

Coral Haskins, MAC, L.Ac.
612-555-0193
www.needlenook-example.com

Font styles to use
Serif
Sans Serif

Colors

Designer to choose colors to be used in the design.

Requirements
Must have
• The project must have NeedleNook logo, promo on the back, and contact information
Nice to have
• I would like to see the colors of the logo used.

```html
<!DOCTYPE html>
<html lang="en">
<head>
<meta charset="utf-8">
<title>NeedleNook Business Card</title>
<link rel="stylesheet" href="https://fonts.googleapis.com/css2?family=Montserrat:wght@600&family=Open+Sans:wght@400;600&display=swap">
<style>
  :root {
    --page: #eef5f2;
    --card-dark: #221613;
    --card-dark-edge: #1a110e;
    --ring-green: #27a57a;
    --brand-teal: #1f9c78;
    --paper: #ffffff;
    --text-light: #f4f1ee;
    --icon-dark: #221613;
    --band-mint: #cfeee0;
  }
  * { margin: 0; padding: 0; box-sizing: border-box; }
  html, body { width: 1200px; height: 1200px; overflow: hidden; background: var(--page); }
  .canvas {
    width: 1200px; height: 1200px;
    display: flex; flex-direction: column; align-items: center; justify-content: center;
    gap: 40px;
  }
  .card {
    position: relative;
    width: 900px; height: 514px;
    background: linear-gradient(135deg, var(--card-dark) 0%, var(--card-dark-edge) 100%);
    overflow: hidden;
    box-shadow: 0 10px 28px rgba(20, 40, 30, 0.18);
  }
  .card-art { position: absolute; inset: 0; width: 100%; height: 100%; }
  .brand-name {
    position: absolute;
    font-family: "Montserrat", sans-serif;
    font-weight: 600;
    color: var(--brand-teal);
    letter-spacing: 0.06em;
    text-transform: uppercase;
    white-space: nowrap;
    display: flex; align-items: center; gap: 16px;
  }
  .brand-dot {
    width: 22px; height: 22px; border-radius: 50%;
    background: var(--brand-teal);
    flex: none;
  }
  .front .brand-name { left: 310px; top: 257px; transform: translate(-50%, -50%); font-size: 44px; }
  .back .brand-name { left: 560px; top: 235px; transform: translate(-50%, -50%); font-size: 44px; }

  .contact {
    position: absolute; left: 640px; top: 110px; width: 230px;
    display: flex; flex-direction: column; align-items: center; gap: 14px;
    font-family: "Open Sans", sans-serif; color: var(--text-light); text-align: center;
  }
  .contact-icon {
    width: 58px; height: 58px; border-radius: 50%; background: var(--paper);
    display: flex; align-items: center; justify-content: center;
  }
  .contact-name { font-size: 25px; line-height: 1.2; margin-bottom: 14px; }
  .contact-phone { font-size: 27px; letter-spacing: 0.03em; }

  .website {
    position: absolute; left: 560px; top: 340px; transform: translateX(-50%);
    display: flex; align-items: center; gap: 10px;
    padding: 6px 22px 6px 10px;
    background: linear-gradient(90deg, rgba(207,238,224,0) 0%, var(--band-mint) 25%, var(--band-mint) 75%, rgba(207,238,224,0) 100%);
    font-family: "Open Sans", sans-serif; font-size: 21px; color: var(--icon-dark);
    white-space: nowrap;
  }

  .promo {
    position: absolute; left: 28px; top: 50%; transform: translateY(-50%);
    width: 270px;
    display: flex; flex-direction: column; align-items: center; gap: 18px;
    font-family: "Open Sans", sans-serif; text-align: center;
  }
  .promo-offer {
    font-size: 30px; font-weight: 600; line-height: 1.2;
    color: var(--text-light);
  }
  .promo-rule { width: 80px; height: 3px; background: var(--ring-green); }
  .promo-tagline {
    font-size: 19px; line-height: 1.45;
    color: var(--ring-green);
  }
</style>
</head>
<body>
<main class="canvas">

  <section class="card front" aria-label="Business card front">
    <svg class="card-art" viewBox="0 0 900 514" aria-hidden="true">
      <circle cx="310" cy="257" r="236" fill="var(--paper)" stroke="var(--ring-green)" stroke-width="14"/>
      <path d="M120 150 A215 215 0 0 0 150 390" fill="none" stroke="var(--ring-green)" stroke-width="3"/>
      <path d="M470 120 A215 215 0 0 1 500 370" fill="none" stroke="var(--ring-green)" stroke-width="3"/>
    </svg>
    <div class="brand-name"><span class="brand-dot"></span>NeedleNook</div>
    <div class="contact">
      <div class="contact-icon">
        <svg width="32" height="36" viewBox="0 0 32 36" aria-label="Location">
          <path d="M16 2 C8 2 3 8 3 14 C3 22 16 34 16 34 C16 34 29 22 29 14 C29 8 24 2 16 2 Z" fill="var(--icon-dark)"/>
          <circle cx="16" cy="14" r="6" fill="var(--paper)"/>
        </svg>
      </div>
      <p class="contact-name">Coral Haskins,<br>MAC, L.Ac.</p>
      <div class="contact-icon">
        <svg width="26" height="34" viewBox="0 0 26 34" aria-label="Phone">
          <rect x="3" y="2" width="20" height="30" rx="3" fill="var(--icon-dark)"/>
          <rect x="6" y="6" width="14" height="10" fill="var(--paper)"/>
          <circle cx="9" cy="21" r="1.6" fill="var(--paper)"/><circle cx="13" cy="21" r="1.6" fill="var(--paper)"/><circle cx="17" cy="21" r="1.6" fill="var(--paper)"/>
          <circle cx="9" cy="26" r="1.6" fill="var(--paper)"/><circle cx="13" cy="26" r="1.6" fill="var(--paper)"/><circle cx="17" cy="26" r="1.6" fill="var(--paper)"/>
        </svg>
      </div>
      <p class="contact-phone">612-555-0193</p>
    </div>
  </section>

  <section class="card back" aria-label="Business card back">
    <svg class="card-art" viewBox="0 0 900 514" aria-hidden="true">
      <circle cx="560" cy="257" r="236" fill="var(--paper)" stroke="var(--ring-green)" stroke-width="14"/>
      <path d="M370 150 A215 215 0 0 0 400 390" fill="none" stroke="var(--ring-green)" stroke-width="3"/>
      <path d="M720 120 A215 215 0 0 1 750 370" fill="none" stroke="var(--ring-green)" stroke-width="3"/>
    </svg>
    <div class="promo">
      <p class="promo-offer">First session<br>free</p>
      <span class="promo-rule"></span>
      <p class="promo-tagline">Refresh, Restore,<br>Rejuvenate</p>
    </div>
    <div class="brand-name"><span class="brand-dot"></span>NeedleNook</div>
    <div class="website">
      <svg width="24" height="24" viewBox="0 0 24 24" aria-label="Website">
        <circle cx="12" cy="12" r="10" fill="none" stroke="var(--icon-dark)" stroke-width="2"/>
        <ellipse cx="12" cy="12" rx="4.5" ry="10" fill="none" stroke="var(--icon-dark)" stroke-width="1.5"/>
        <line x1="2" y1="12" x2="22" y2="12" stroke="var(--icon-dark)" stroke-width="1.5"/>
        <line x1="4" y1="7" x2="20" y2="7" stroke="var(--icon-dark)" stroke-width="1.2"/>
        <line x1="4" y1="17" x2="20" y2="17" stroke="var(--icon-dark)" stroke-width="1.2"/>
      </svg>
      <span>www.needlenook-example.com</span>
    </div>
  </section>

</main>
</body>
</html>
```